Real Estate Investor needs awesome business card design

I invest in real estate, focused on multi-family properties, and I need a business card to hand out to potential partners. I prefer simple, clean designs, but it needs to stand out, so I'd like there to be a bit of red in the design as well.

It should include this information:

Front
Dallin Pecksworth
Real Estate Investor
Direct phone: 502-867-3394
Email: dallinhpecksworth@quillmail.example
Headshot (Picture), I've uploaded a few, just pick the one you think looks best with your design. You can remove the background from the headshot image if it looks better.

Back
The back of the card's design should flow and be congruent with the front. On the back I want to put an inspirational quote or question. There will be different ones depending on the card, so I'll need the original file so I can edit it in the end.

For now, use “The Pessimist Sees Difficulty In Every Opportunity. The Optimist Sees The Opportunity In Every Difficulty.” -Barnaby Ellsworth

Target Market(s)

Investors

Industry/Entity Type

Real Estate

Contact Information for Business Card

Front
Dallin Pecksworth
Real Estate Investor

Back
The back of the card's design should flow and be congruent with the front. On the back I want to put an inspirational quote or question. There will be different ones depending on the card, so I'll need the original file so I can edit it in the end. I've uploaded some EXAMPLES of business cards with quotes on them. Don't copy but feel free to use them as inspiration.

The design will be printed on "ZIB sized" business cards
1039 x 697 pixels
with rounded corners

Font styles to use
Serif
Decorative
Script

Colors
ec1f27

Requirements
Must have
• Headshot, name, and other information in it.
• 1039 x 697 pixels
• Rounded corners
• Clean design that pops. I'm open to see any color background, including black.
• Headshots can be located here: https://www.filecrate.example/sh/8kd2wq7mzt31hvx/BBQTXP4ruf9LmQ0KhcvWx7b?dl=0
Nice to have
• It would be awesome if the design included a personal signature or monogram, but if not I'll get a personal logo developed later and the card redesigned if I think it needs it.
Should not have
• Cluttered design

```html
<!DOCTYPE html>
<html lang="en">
<head>
<meta charset="utf-8">
<title>Dallin Pecksworth – Business Card</title>
<link rel="stylesheet" href="https://fonts.googleapis.com/css2?family=Jost:wght@300;400&family=Open+Sans:wght@400;600&display=swap">
<style>
  :root {
    --red: #ec1f27;
    --ink: #1a1a1a;
    --paper: #ffffff;
    --stage: #9a9a9a;
    --photo-dark: #1e1e1e;
    --photo-mid: #4a4a4a;
  }
  * { box-sizing: border-box; margin: 0; padding: 0; }
  html, body { width: 1200px; height: 1200px; overflow: hidden; }
  body {
    background: var(--stage);
    display: flex;
    flex-direction: column;
    align-items: center;
    justify-content: center;
    gap: 48px;
    font-family: "Open Sans", sans-serif;
  }
  .card {
    width: 780px;
    height: 523px;
    background: var(--paper);
    border-radius: 18px;
    overflow: hidden;
    position: relative;
    box-shadow: 0 6px 18px rgba(0,0,0,0.18);
  }

  /* Front */
  .card-front { display: flex; }
  .headshot {
    width: 372px;
    height: 100%;
    background: radial-gradient(ellipse at 45% 45%, var(--photo-mid) 0%, var(--photo-dark) 75%);
  }
  .accent-stripe { width: 10px; height: 100%; background: var(--red); }
  .front-info {
    flex: 1;
    position: relative;
    padding: 58px 46px 54px 44px;
  }
  .name {
    font-family: "Jost", sans-serif;
    font-weight: 300;
    font-size: 40px;
    letter-spacing: 2px;
    line-height: 1;
    color: var(--ink);
    text-transform: uppercase;
    white-space: nowrap;
  }
  .title {
    margin-top: 8px;
    font-size: 21px;
    color: var(--red);
    padding-left: 150px;
  }
  .contact-list {
    position: absolute;
    right: 40px;
    bottom: 56px;
    list-style: none;
    display: flex;
    flex-direction: column;
    align-items: flex-end;
    gap: 10px;
  }
  .contact-item {
    display: flex;
    align-items: center;
    gap: 12px;
    font-size: 19px;
    color: var(--ink);
  }
  .contact-icon { width: 26px; height: 26px; flex: none; }

  /* Back */
  .card-back {
    display: flex;
    flex-direction: column;
    justify-content: center;
    padding: 0 70px;
  }
  .quote {
    font-size: 20px;
    line-height: 1.6;
    color: var(--ink);
    text-align: center;
  }
  .quote-author {
    margin-top: 16px;
    font-size: 17px;
    color: var(--red);
    text-align: center;
  }
  .back-surname {
    margin-top: 44px;
    font-family: "Jost", sans-serif;
    font-weight: 300;
    font-size: 60px;
    letter-spacing: 4px;
    text-align: center;
    color: var(--ink);
    text-transform: uppercase;
  }
  .back-stripe {
    position: absolute;
    left: 0; right: 0; bottom: 0;
    height: 10px;
    background: var(--red);
  }
</style>
</head>
<body>

  <section class="card card-front" aria-label="Card front">
    <div class="headshot" role="img" aria-label="Black and white headshot of Dallin Pecksworth in a dark suit"></div>
    <div class="accent-stripe"></div>
    <div class="front-info">
      <h1 class="name">Dallin Pecksworth</h1>
      <p class="title">Real Estate Investor</p>
      <ul class="contact-list">
        <li class="contact-item">
          <span>502-867-3394</span>
          <svg class="contact-icon" viewBox="0 0 26 26" aria-hidden="true">
            <rect width="26" height="26" fill="var(--red)"/>
            <path d="M8 6.5c1-.6 1.8-.4 2.3.5l1 2c.3.7.1 1.3-.5 1.7l-.8.5c.7 1.7 1.9 2.9 3.6 3.6l.5-.8c.4-.6 1-.8 1.7-.5l2 1c.9.5 1.1 1.3.5 2.3-.8 1.4-2.3 1.9-4 1.2-3.3-1.3-5.8-3.8-7.1-7.1-.7-1.7-.2-3.2 1.2-4z" fill="#fff"/>
          </svg>
        </li>
        <li class="contact-item">
          <span>dallinhpecksworth@quillmail.example</span>
          <svg class="contact-icon" viewBox="0 0 26 26" aria-hidden="true">
            <rect width="26" height="26" fill="var(--red)"/>
            <rect x="5" y="8" width="16" height="11" fill="none" stroke="#fff" stroke-width="1.6"/>
            <path d="M5 8l8 6.5L21 8" fill="none" stroke="#fff" stroke-width="1.6"/>
          </svg>
        </li>
      </ul>
    </div>
  </section>

  <section class="card card-back" aria-label="Card back">
    <p class="quote">“The Pessimist Sees Difficulty In Every Opportunity. The Optimist Sees The Opportunity In Every Difficulty.”</p>
    <p class="quote-author">– Barnaby Ellsworth</p>
    <p class="back-surname">Pecksworth</p>
    <div class="back-stripe"></div>
  </section>

</body>
</html>
```